A home-based beauty salon needs a website

Creation of an aesthetically pleasing and user-friendly website, crucial for showcasing our products, services and driving customer engagement/online bookings.

Focusing on key elements:
- mobile compatibility (fast loading on mobile)
- accessibility
- well-planned information architecture
- effective navigation
- simple forms (Contact Us)
- blog
- online store (e.g. shopify) to sell beauty products
- newsletter subscription
- online booking: integrate with existing engine = Fresha
- easy ongoing maintenance

Objective of website:
- Build online brand presence: classy, aesthetic and professional
- Drive online bookings
- Drive online sales

Services offered:
- Laser Hair Removal
- Chemical Peels
- Advanced Skin Treatments
- LED Light Therapy
- Teeth Whitening

Inspiration:
Ideal layout and function: https://velinorskin.ca/
Innovative and sleek design: https://www.studiotavi.sk/

Pictogrove: https://www.pictogrove.com/bramelskin_official/

Colour preferences: Black, White, and if possible Tropical Rainforest Palm Leave greens to match our feature-wall in the clinic room (see uploaded files for example behind our business logo). Open to seeing light pastel colours as well.

Copy: to be provided post design-phase
Images: of the clinic and our machines can be provided during design-phase
Font style: fancy and light to match the logo

Sections:
Home, About, Spa (Hydro-dermabrasion, LED Light Therapy, Peels, Facials, Signature Packages), Medical (Laser Hair Removal, Chemical Peels, Teeth Whitening), Contact, Blog

Industry/Entity Type

Beauty and Skincare Industry

Coding

Coded - Design and coding required

Number of Pages Required

5+ page

Colors

Designer to choose colors to be used in the design.

Requirements
Must have
• Integration with Shopify or similar, Integration with Splitly or Paylo Pay, Newsletter subscription pop-up or similar, Map to visualise location and make it easy for customers to find us, Integration with our Fresha booking engine, Integration with Pictogrove or Gallery under each service offering to present before vs after images of treatments to support the Consideration process
Nice to have
• (1) Contact Us Page: form + visual navigation of how to get to the clinic to make it easy to find us. (2) Online Store integration with Shopify. (3) Integrate Gallery or select Pictogrove pictures that match the service offered to help customers see potential results when selecting services. e.g. Teeth Whitening before and after on the Teeth Whitening service page. (4) Integrate Paylo Pay or Splitly next to product/service offers making it easy to understand potential repayments . (5)

```html
<!DOCTYPE html>
<html lang="en">
<head>
<meta charset="utf-8">
<title>Bramel Skin — Beauty &amp; Skincare</title>
<link href="https://fonts.googleapis.com/css2?family=Cormorant+Garamond:wght@400;500&family=Jost:wght@400;500&display=swap" rel="stylesheet">
<style>
:root{
  --ink:#121314;
  --white:#ffffff;
  --green:#0b7a57;
  --green-dark:#08654a;
  --teal:#4db3a3;
  --blush:#fdf0ee;
  --mist:#e8f3f5;
  --footer:#e5f1f1;
  --text:#2a2a2a;
  --muted:#6b6b6b;
  --serif:'Cormorant Garamond', 'Times New Roman', serif;
  --sans:'Jost', Arial, sans-serif;
}
*{box-sizing:border-box;margin:0;padding:0}
html,body{width:1200px;height:4409px;overflow:hidden;background:var(--white)}
body{font-family:var(--sans);color:var(--text)}
section,header,footer{position:relative;width:1200px;overflow:hidden}
.abs{position:absolute}
.photo{position:absolute;display:block}
.section-title{position:absolute;left:0;width:1200px;text-align:center;font-family:var(--serif);font-weight:500;font-size:40px;color:var(--ink)}
.btn-outline{position:absolute;display:flex;align-items:center;justify-content:center;border:1.5px solid var(--green);font-size:11px;color:var(--green);font-weight:500}

/* header */
.site-header{height:78px;background:var(--ink)}
.brand{position:absolute;left:225px;top:8px;width:92px;height:92px;border-radius:50%;background:var(--ink);display:flex;align-items:center;justify-content:center;font-family:var(--serif);font-size:22px;color:var(--white);z-index:2}
.nav{position:absolute;left:380px;top:0;height:78px;display:flex;align-items:center;gap:36px;font-size:11px;color:var(--white);letter-spacing:.5px}
.nav .dot{width:8px;height:8px;border-radius:50%;background:var(--green)}
.nav .caret::after{content:" ▾";font-size:8px}
.btn-book{position:absolute;left:815px;top:20px;width:110px;height:38px;background:var(--green);color:var(--white);font-size:11px;display:flex;align-items:center;justify-content:center}

/* hero */
.hero{height:479px;background:linear-gradient(100deg,#6b5a55 0%,#8e7f7a 35%,#c9b5a6 60%,#e8d9cd 80%,#d9c8bb 100%)}
.hero h1{position:absolute;left:200px;top:140px;font-family:var(--serif);font-weight:400;font-size:42px;line-height:50px;color:var(--white)}
.hero p{position:absolute;left:200px;top:250px;font-family:var(--serif);font-size:16px;color:var(--white)}
.hero .btn-contact{position:absolute;left:200px;top:298px;width:114px;height:36px;border:1.5px solid var(--green);background:rgba(11,122,87,.25);color:var(--white);font-size:11px;display:flex;align-items:center;justify-content:center}

/* services */
.services{height:694px;background:var(--blush)}
.services .section-title{top:60px}
.service-tile{position:absolute;width:250px;height:235px;display:flex;align-items:flex-end;justify-content:center;padding-bottom:22px;font-family:var(--serif);font-size:18px;color:var(--white)}
.service-tile.peels{background:var(--teal);align-items:center;padding:0;text-align:center;line-height:22px}
.service-tile.peels .frame{position:absolute;left:18px;top:18px;right:18px;bottom:18px;border:1px solid rgba(255,255,255,.6)}
.service-tile.book{align-items:center;padding:0}
.service-tile.book .ring{position:absolute;left:35px;top:27px;width:180px;height:180px;border-radius:50%;border:1px solid rgba(255,255,255,.7);background:rgba(255,255,255,.12)}

/* about */
.about{height:761px;background:var(--green)}
.about h2{position:absolute;left:293px;top:62px;font-family:var(--serif);font-weight:400;font-size:40px;line-height:50px;color:var(--white)}
.about p{position:absolute;left:293px;top:188px;width:600px;font-family:var(--serif);font-size:11.5px;line-height:19px;color:var(--white)}
.about .btn-discover{position:absolute;left:293px;top:277px;width:112px;height:36px;border:1.5px solid var(--white);color:var(--white);font-size:10px;display:flex;align-items:center;justify-content:center}

/* shop */
.shop{height:474px;background:var(--mist)}
.shop .section-title{top:58px}
.product{position:absolute;top:138px;width:182px}
.product .photo{position:relative;width:182px;height:164px}
.product span{display:block;text-align:center;margin-top:24px;font-family:var(--serif);font-size:13px;color:var(--text)}
.btn-solid{position:absolute;left:546px;top:371px;width:111px;height:35px;background:var(--green);color:var(--white);font-size:10px;display:flex;align-items:center;justify-content:center}

/* articles */
.articles{height:636px;background:var(--white)}
.articles .section-title{top:66px}
.articles .lead{position:absolute;left:400px;top:124px;width:400px;text-align:center;font-size:9px;line-height:15px;color:var(--muted)}
.date{font-size:8px;color:var(--green);font-weight:500;letter-spacing:.3px}
.feature-title{position:absolute;left:200px;top:450px;width:360px;font-family:var(--serif);font-weight:400;font-size:16px;line-height:16px;color:var(--ink)}
.article-row{position:absolute;left:637px;width:363px;height:101px;border-top:1px solid #e6e6e6;display:flex;align-items:center;gap:24px}
.article-row .photo{position:relative;width:105px;height:95px}
.article-row h3{font-family:var(--serif);font-weight:400;font-size:14px;line-height:17px;color:var(--ink);margin-top:8px}

/* newsletter */
.newsletter{height:330px;background:linear-gradient(90deg,#f7efe8 0%,#fbf3ee 40%,#fbf1ec 70%,#f5e6e0 100%)}
.newsletter .section-title{top:72px}
.newsletter .sub{position:absolute;left:0;width:1200px;top:132px;text-align:center;font-size:12px;color:var(--ink)}
.field{position:absolute;top:164px;width:263px;height:28px;border:1px solid #b9b2ad;background:var(--white);font-size:9px;color:var(--muted);padding-left:10px;display:flex;align-items:center}

/* gallery feed */
.feed{height:560px}
.feed-title{position:absolute;left:0;top:66px;width:1200px;text-align:center;font-family:var(--serif);font-weight:500;font-size:36px;color:var(--ink)}

/* footer */
.site-footer{height:397px;background:var(--footer)}
.foot-brand{position:absolute;left:200px;top:110px;font-family:var(--serif);font-size:34px;color:var(--ink)}
.foot-col h4{font-family:var(--serif);font-weight:500;font-size:15px;color:var(--ink);margin-bottom:18px}
.foot-col{position:absolute;top:72px;font-size:9px;color:var(--text)}
.foot-col li{list-style:none;height:21px}
.contact-line{display:flex;gap:10px;align-items:flex-start;margin-bottom:14px;line-height:14px}
.social{display:flex;gap:10px;margin-top:8px}
.social span{width:26px;height:26px;border-radius:50%;display:block}
.copyright{position:absolute;left:200px;top:350px;font-size:8px;color:var(--text)}
.copyright b{color:var(--green);font-weight:500}
.pay{position:absolute;top:344px;font-size:15px;font-weight:500;color:var(--ink)}
</style>
</head>
<body>

<header class="site-header">
  <div class="brand">Bramel</div>
  <nav class="nav">
    <span class="dot"></span>
    <span>ABOUT</span>
    <span class="caret">SPA</span>
    <span class="caret">MEDICAL</span>
    <span>CONTACT</span>
    <span>BLOG</span>
  </nav>
  <a class="btn-book">Book Now!</a>
</header>

<section class="hero" role="img" aria-label="Woman in a white robe applying face cream at a bright salon window">
  <h1>Lorem ipsum is simply<br>typesetting industry.</h1>
  <p>It is a long established fact that a reader</p>
  <a class="btn-contact">Contact Us</a>
</section>

<section class="services">
  <h2 class="section-title">Service we provide</h2>
  <div class="service-tile" style="left:200px;top:127px;background:linear-gradient(160deg,#d8d4d3,#9b8e87)" role="img" aria-label="Laser hair removal treatment on a leg">Laser Hair Removal</div>
  <div class="service-tile peels" style="left:476px;top:127px"><span class="frame"></span>Chemical Peels<br>$15</div>
  <div class="service-tile" style="left:751px;top:127px;background:linear-gradient(160deg,#c9d7de,#7f98a4)" role="img" aria-label="Client receiving an advanced skin treatment">Advanced Skin Treatments</div>
  <div class="service-tile" style="left:200px;top:386px;background:linear-gradient(160deg,#3a5d7c,#8a3f3f)" role="img" aria-label="LED light therapy mask session">LED Light Therapy</div>
  <div class="service-tile" style="left:476px;top:386px;background:linear-gradient(160deg,#6a4b3c,#c29a82)" role="img" aria-label="Smiling woman after teeth whitening">Teeth Whitening</div>
  <div class="service-tile book" style="left:751px;top:386px;background:linear-gradient(160deg,#b4aca7,#6f6763)" role="img" aria-label="Woman in a towel turban"><span class="ring"></span><span style="position:relative">Book Now!</span></div>
</section>

<section class="about">
  <h2>Contrary to popular belief, ipsum<br>is not simply random text.</h2>
  <p>There are many variations of passages of Lorem Ipsum available, but the majority have suffered alteration in some form, by injected humour, or randomised words which don't look even slightly believable. If you are going to use a passage of Lorem Ipsum, you need to be sure there isn't anything embarrassing hidden in the middle of text.</p>
  <a class="btn-discover">Discover More</a>
  <div class="photo" style="left:0;top:384px;width:519px;height:248px;background:linear-gradient(90deg,#4e7a3a,#d9b8a4 40%,#d8b6a0 70%,#5f8a3d)" role="img" aria-label="Smiling woman beside palm leaves"></div>
  <div class="photo" style="left:670px;top:384px;width:530px;height:377px;background:linear-gradient(180deg,#e6ddd3,#c8b7a6 60%,#5a4c42)" role="img" aria-label="Clinic treatment room with a treatment bed"></div>
</section>

<section class="shop">
  <h2 class="section-title">Shop our products</h2>
  <div class="product" style="left:200px"><div class="photo" style="background:linear-gradient(150deg,#ece8e2,#8c6e55)" role="img" aria-label="Cream jar and serum bottle"></div><span>Products Name</span></div>
  <div class="product" style="left:406px"><div class="photo" style="background:linear-gradient(150deg,#cfe6ea,#6bb5bf)" role="img" aria-label="Skincare bottles on turquoise"></div><span>Products Name</span></div>
  <div class="product" style="left:612px"><div class="photo" style="background:linear-gradient(150deg,#f1f1ef,#7a5a3a)" role="img" aria-label="Amber dropper bottles with greenery"></div><span>Products Name</span></div>
  <div class="product" style="left:818px"><div class="photo" style="background:linear-gradient(150deg,#f6d7c3,#e4a988)" role="img" aria-label="Cream tube on peach background"></div><span>Products Name</span></div>
  <a class="btn-solid">Shop Now!</a>
</section>

<section class="articles">
  <h2 class="section-title">Recent articles</h2>
  <p class="lead">Lorem Ipsum is simply dummy text of the printing and typesetting industry. Lorem Ipsum has been the industry's standard dummy</p>
  <div class="photo" style="left:200px;top:179px;width:389px;height:224px;background:linear-gradient(120deg,#d7d0cb,#f2ece8 50%,#c9bfb8)" role="img" aria-label="Woman in a towel applying skincare"></div>
  <div class="abs date" style="left:200px;top:430px">MAY-20-2023</div>
  <h3 class="feature-title">Lorem ipsum is text simply dummy text of the<br>and typesetting industry.</h3>

  <div class="article-row" style="top:184px"><div class="photo" style="background:linear-gradient(150deg,#d9d6d3,#8c8480)" role="img" aria-label="Facial treatment"></div><div><div class="date">MAY-20-2023</div><h3>Lorem Ipsum is text simply<br>dummy text of the</h3></div></div>
  <div class="article-row" style="top:292px"><div class="photo" style="background:linear-gradient(150deg,#cfe4c7,#e0a24a)" role="img" aria-label="Skincare ingredients"></div><div><div class="date">MAY-20-2023</div><h3>Lorem Ipsum is text simply<br>dummy text of the</h3></div></div>
  <div class="article-row" style="top:400px;border-bottom:1px solid #e6e6e6"><div class="photo" style="background:linear-gradient(150deg,#e9d4cc,#9a5145)" role="img" aria-label="Woman with a cosmetic product"></div><div><div class="date">MAY-20-2023</div><h3>Lorem Ipsum is text simply<br>dummy text of the</h3></div></div>

  <a class="btn-outline" style="left:550px;top:536px;width:107px;height:30px">View All</a>
</section>

<section class="newsletter">
  <div class="photo" style="left:0;top:0;width:256px;height:330px;background:linear-gradient(160deg,#587c3c,#e8e2da 55%,#cfc3b5)" role="img" aria-label="Palm leaf, towels and bath brush"></div>
  <div class="photo" style="left:946px;top:0;width:254px;height:330px;background:linear-gradient(200deg,#e7c9b8,#f6ece6 55%,#f4eeea)" role="img" aria-label="Woman's face with white orchids"></div>
  <h2 class="section-title">Subscribe newsletter</h2>
  <p class="sub">Subscribe for a weekly dose of skincare and beauty.</p>
  <div class="field" style="left:331px">Name</div>
  <div class="field" style="left:606px">Email ...</div>
  <a class="btn-outline" style="left:546px;top:218px;width:110px;height:28px;background:var(--white)">Subscribe</a>
</section>

<section class="feed">
  <h2 class="feed-title">bramelskin_official</h2>
  <div class="photo" style="left:200px;top:138px;width:313px;height:293px;background:linear-gradient(150deg,#d8d2cb,#f1ede8 50%,#b3aaa2)" role="img" aria-label="Woman in a robe reading in bed"></div>
  <div class="photo" style="left:526px;top:138px;width:148px;height:140px;background:linear-gradient(150deg,#f3d3da,#c9a068)" role="img" aria-label="Gold decorative object on pink"></div>
  <div class="photo" style="left:688px;top:138px;width:149px;height:140px;background:linear-gradient(150deg,#d6d6d6,#3a3330)" role="img" aria-label="Portrait against leaves"></div>
  <div class="photo" style="left:850px;top:138px;width:152px;height:140px;background:linear-gradient(150deg,#f2eeeb,#c0868a)" role="img" aria-label="Row of skincare bottles"></div>
  <div class="photo" style="left:526px;top:291px;width:148px;height:140px;background:linear-gradient(150deg,#e7c5ae,#5b4a40)" role="img" aria-label="Relaxing facial treatment"></div>
  <div class="photo" style="left:688px;top:291px;width:149px;height:140px;background:linear-gradient(150deg,#d8c7ae,#9e8266)" role="img" aria-label="Gold accessories flatlay"></div>
  <div class="photo" style="left:850px;top:291px;width:152px;height:140px;background:linear-gradient(150deg,#2b3c9a,#0c1240)" role="img" aria-label="Blue LED therapy session"></div>
  <a class="btn-outline" style="left:513px;top:461px;width:174px;height:28px">Follow Us on Pictogrove</a>
</section>

<footer class="site-footer">
  <div class="foot-brand">Bramel Skin</div>

  <div class="foot-col" style="left:404px;width:200px">
    <h4>Contact us</h4>
    <div class="contact-line" style="font-size:11px">
      <svg width="10" height="12" viewBox="0 0 24 24" aria-hidden="true"><path d="M6 2l4 4-2 3c1 3 4 6 7 7l3-2 4 4-3 4C10 21 3 14 2 5z" fill="#0b7a57"/></svg>
      <span>(99) 5120 4471</span>
    </div>
    <div class="contact-line">
      <svg width="10" height="10" viewBox="0 0 24 24" aria-hidden="true"><rect x="2" y="5" width="20" height="14" fill="none" stroke="#0b7a57" stroke-width="2"/><path d="M2 5l10 8 10-8" fill="none" stroke="#0b7a57" stroke-width="2"/></svg>
      <span>hello@bramelskin.com.au</span>
    </div>
    <div class="contact-line">
      <svg width="10" height="12" viewBox="0 0 24 24" aria-hidden="true"><path d="M12 1a8 8 0 0 0-8 8c0 6 8 14 8 14s8-8 8-14a8 8 0 0 0-8-8zm0 11a3 3 0 1 1 0-6 3 3 0 0 1 0 6z" fill="#0b7a57"/></svg>
      <span>12 Fernleaf Circuit,<br>Harbour Vale, NSW, Australia,<br>New South Wales</span>
    </div>
    <div class="social"><span style="background:var(--ink)"></span><span style="background:var(--green)"></span></div>
  </div>

  <div class="foot-col" style="left:655px">
    <h4>Quick links</h4>
    <ul><li>Home</li><li>About</li><li>Spa</li><li>Medical</li><li>Blog</li><li>Contact</li></ul>
  </div>

  <div class="foot-col" style="left:818px">
    <h4>Services</h4>
    <ul><li>Laser Hair Removal</li><li>Chemical Peels</li><li>Advanced Skin Treatments</li><li>LED Light Therapy</li><li>Teeth Whitening</li></ul>
  </div>

  <p class="copyright">© 2024 <b>BRAMEL SKIN</b>. All Right Reserved</p>
  <span class="pay" style="left:655px">Paylo</span>
  <span class="pay" style="left:724px">Splitly</span>
  <svg class="abs" style="left:1082px;top:344px" width="14" height="16" viewBox="0 0 14 16" aria-label="Back to top"><path d="M7 0L14 16 7 11 0 16z" fill="#0b7a57"/></svg>
</footer>

</body>
</html>
```